Brochure Design for B-to-B software company

This project is for a product brochure in an 11x17 bifold format. The brochure will be a printed on heavy stock that will fold into 4 - 8 ½” x 11” pages. The folded edge will be on the left side. The brochure will be a combination of text and graphics. The completed editable files will be provided to us for further edits when needed. The color palette should complement and not overuse our logo colors.

Target Market(s)

Corporate Brands

Font styles to use
Sans Serif

Colors
cadf82

Requirements
Must have
• Color palette described in attached project overview document

```html
<!DOCTYPE html>
<html lang="en">
<head>
<meta charset="utf-8">
<title>Verdalia CRM – B-to-B Sales Channel Brochure</title>
<link href="https://fonts.googleapis.com/css2?family=Montserrat:wght@600;700;800&family=Open+Sans:wght@400;600&display=swap" rel="stylesheet">
<style>
  :root{
    --green:#6cc04a;
    --green-light:#cadf82;
    --green-bright:#8fd14f;
    --green-deep:#3f9a2a;
    --slate:#3e4452;
    --slate-soft:#5a6070;
    --ink:#4a4a4a;
    --paper:#ffffff;
    --stage:#727272;
    --orange:#f39a1e;
    --blue:#2a8fe0;
  }
  *{box-sizing:border-box;margin:0;padding:0}
  html,body{width:1200px;height:2442px;overflow:hidden}
  body{background:var(--stage);font-family:"Open Sans",Arial,sans-serif;color:var(--ink);position:relative}

  .sheet{position:absolute;left:0;width:1200px;height:814px}
  .sheet--cover{top:0}
  .sheet--inside{top:814px;border-top:1px solid #666}
  .sheet--outside{top:1628px;border-top:1px solid #666}

  .page{position:absolute;top:51px;width:550px;height:712px;background:var(--paper);overflow:hidden}
  .sheet--cover .page{left:325px}
  .page--left{left:50px}
  .page--right{left:600px}
  .page--left::after{content:"";position:absolute;top:0;right:0;width:24px;height:100%;background:linear-gradient(to left,rgba(0,0,0,.12),rgba(0,0,0,0))}
  .page--right::before{content:"";position:absolute;top:0;left:0;width:24px;height:100%;background:linear-gradient(to right,rgba(0,0,0,.1),rgba(0,0,0,0));z-index:3}

  .abs{position:absolute}
  .brand{font-family:"Montserrat",sans-serif;font-weight:700;color:var(--green);display:flex;align-items:center;gap:7px;white-space:nowrap}
  .brand__dot{width:11px;height:11px;border-radius:50%;background:var(--green)}

  /* cover */
  .cover__brand{top:30px;left:0;width:100%;justify-content:center;font-size:22px}
  .cover__title{top:70px;left:0;width:100%;text-align:center;font-family:"Montserrat",sans-serif;font-weight:800;text-transform:uppercase;line-height:1.15}
  .cover__title .t1{display:block;color:var(--green);font-size:19px}
  .cover__title .t2{display:block;color:var(--slate);font-size:15px}
  .kicker{font-family:"Montserrat",sans-serif;font-weight:700;color:var(--green);text-transform:uppercase;font-size:9.5px;letter-spacing:.2px}
  .cover__intro{top:122px;left:36px;width:480px}
  .cover__intro p{font-size:8.6px;line-height:1.35;margin-top:4px}
  .feature h3{font-family:"Montserrat",sans-serif;font-weight:700;color:var(--green);text-transform:uppercase;font-size:9.5px;line-height:1.2;margin-bottom:4px}
  .feature p{font-size:8.6px;line-height:1.35;margin:0 0 6px 10px}
  .feature + .feature{margin-top:10px}
  .col-left{top:205px;left:36px;width:160px}
  .col-right{top:196px;left:360px;width:160px}
  .col-bottom-left{top:360px;left:36px;width:160px}
  .col-bottom-mid{top:352px;left:204px;width:148px}
  .chart{top:200px;left:196px;width:160px;height:140px}
  .leaf-spot{position:absolute;left:0;top:60px;width:46px;height:40px;border-radius:50%;background:radial-gradient(circle,#4f9b2a,#7cc44a 70%,rgba(124,196,74,0) 72%)}

  .band-bottom{left:0;bottom:0;width:550px;height:200px}
  .site{font-family:"Montserrat",sans-serif;font-weight:600;font-size:15px;display:flex;align-items:center;gap:10px;white-space:nowrap}
  .site::before,.site::after{content:"";width:44px;height:1.5px;background:currentColor;opacity:.85}
  .cover__site{bottom:46px;left:0;width:100%;justify-content:center;color:#fff}

  /* inside */
  .band-top{top:0;left:0;width:550px;height:130px}
  .inside__body{top:126px;left:36px;width:484px}
  .inside__body h2{font-family:"Montserrat",sans-serif;font-weight:800;color:var(--green);text-transform:uppercase;font-size:14px;line-height:1.2;margin-top:12px}
  .inside__body h2:first-child{margin-top:0}
  .inside__body h4{font-family:"Montserrat",sans-serif;font-weight:700;color:var(--slate);font-size:11px;margin-top:2px}
  .inside__body p{font-size:9.4px;line-height:1.42;margin-top:3px}
  .inside__body h2 .num{color:var(--slate)}
  .inside-left__site{bottom:30px;left:36px;color:var(--slate)}
  .inside-left__site::after{background:var(--green)}
  .inside-left__site::before{background:var(--green)}
  .inside-right__body{top:150px}
  .inside-right__brand{bottom:86px;right:40px;font-size:24px}
  .corner-bottom{right:0;bottom:0;width:550px;height:110px}

  /* back */
  .back__swoosh{top:0;left:0;width:550px;height:110px}
  .plans{top:80px;left:28px;width:494px;border-collapse:collapse;font-family:"Montserrat",sans-serif}
  .plans th{height:34px;background:var(--green);color:#fff;font-size:8.5px;font-weight:700;border:1px solid rgba(255,255,255,.55)}
  .plans th.blank{background:transparent;border:none}
  .plans td{height:36px;border:1px solid rgba(255,255,255,.55)}
  .plans td.feat{width:236px;background:var(--slate);color:#fff;padding:3px 8px;vertical-align:middle;border-color:#5a6070}
  .plans td.feat b{display:block;font-size:8.6px;font-weight:700}
  .plans td.feat span{display:block;font-family:"Open Sans",sans-serif;font-size:6.6px;line-height:1.25;color:#d5d8de}
  .plans td.mark{background:var(--green);color:#fff;text-align:center;font-size:11px;font-weight:700;width:86px}
  .plans tr:nth-child(even) td.mark{background:#78c957}
  .back__contact{left:0;bottom:0;width:550px;height:190px}
  .touch{bottom:96px;left:130px;font-family:"Montserrat",sans-serif;font-weight:800;font-size:24px;color:var(--slate);letter-spacing:.5px;text-transform:uppercase}
  .contact-line{font-family:"Montserrat",sans-serif;font-weight:600;color:#fff;font-size:12px;display:flex;align-items:center;gap:7px;white-space:nowrap}
  .contact-mail{bottom:64px;left:200px}
  .contact-phone{bottom:28px;left:30px}
  .social{bottom:96px;right:36px;display:flex;gap:6px}
  .social i{display:block;width:14px;height:14px;border-radius:50%;background:#fff}
</style>
</head>
<body>

<!-- ===== Front cover ===== -->
<section class="sheet sheet--cover">
  <article class="page cover">
    <svg class="abs" style="top:0;left:0" width="120" height="60" viewBox="0 0 120 60" aria-hidden="true">
      <path d="M0 52 Q10 18 60 0 L38 0 Q8 14 0 36Z" fill="var(--green)"/>
    </svg>
    <div class="abs brand cover__brand"><span class="brand__dot"></span>Verdalia CRM</div>
    <h1 class="abs cover__title"><span class="t1">B-to-B Sales Channel Management</span><span class="t2">For the Cannabis Industry</span></h1>
    <div class="abs cover__intro">
      <div class="kicker">Accelerate sales growth and scale-up quickly</div>
      <p>Developing a B-to-B sales channel can dramatically increase sales growth that complements your retail, marketplace and distributor initiatives.</p>
      <p>The Verdalia CRM B-to-B Sales Channel Management Solution is key to managing that growth and differentiating from competitors. Using our configurable and scalable sales portal CRM technology benefits both you and your customers.</p>
    </div>

    <div class="abs col-left">
      <div class="feature">
        <h3>Branded sales and CRM portal</h3>
        <p>Launch quickly with your branding, products and content</p>
        <p>Allow approved retailers to place sales orders and access CoAs, marketing content and videos</p>
      </div>
    </div>

    <div class="abs chart">
      <div class="leaf-spot" role="img" aria-label="Cannabis leaf illustration"></div>
      <svg class="abs" style="left:40px;top:0" width="120" height="140" viewBox="0 0 120 140" aria-hidden="true">
        <path d="M6 120 L106 128 L116 112 L16 104Z" fill="#dde6ee"/>
        <g fill="var(--blue)">
          <rect x="14" y="100" width="8" height="10"/>
          <rect x="25" y="94" width="8" height="16"/>
          <rect x="36" y="88" width="8" height="22"/>
          <rect x="47" y="80" width="8" height="30"/>
          <rect x="58" y="70" width="8" height="40"/>
          <rect x="69" y="58" width="8" height="52"/>
          <rect x="80" y="44" width="8" height="66"/>
          <rect x="91" y="28" width="9" height="82"/>
        </g>
        <path d="M6 100 Q60 92 78 30" fill="none" stroke="var(--orange)" stroke-width="4"/>
        <path d="M70 32 L80 10 L88 36Z" fill="var(--orange)"/>
      </svg>
    </div>

    <div class="abs col-right">
      <div class="feature">
        <h3>Manage orders through fulfillment</h3>
        <p>Manage products, discounts and inventory in easy-to-use dashboards</p>
        <p>Manage sales orders using automated workflow rules and notifications</p>
        <p>Direct orders to retailer locations</p>
        <p>Alert fulfillment teams as orders become ready for shipment</p>
      </div>
      <div class="feature">
        <h3>Grow and manage your retail sales channel</h3>
        <p>Manage retailer leads</p>
        <p>Manage on-site marketing activities Manage Co-op marketing programs</p>
        <p>Track retailer performance</p>
      </div>
    </div>

    <div class="abs col-bottom-mid">
      <div class="feature">
        <h3>Compliance and tracking</h3>
        <p>Capture and track license status for retailer locations</p>
        <p>View audit trail for complete sales history. Make CoAs available for download at any time</p>
      </div>
    </div>
    <div class="abs col-bottom-left" style="top:380px">
      <div class="feature">
        <h3>Pipeline and sales analytics</h3>
        <p>Track order status and pipeline with performance dashboards</p>
        <p>Analyze order and product sales trends</p>
        <p>View real-time key performance indicators (KPIs) for retailers</p>
      </div>
    </div>

    <svg class="abs band-bottom" viewBox="0 0 550 200" role="img" aria-label="Band of green cannabis leaf photography">
      <defs>
        <linearGradient id="leafBandA" x1="0" y1="0" x2="1" y2="1">
          <stop offset="0" stop-color="#9bd85a"/><stop offset=".55" stop-color="#5cb638"/><stop offset="1" stop-color="#8ed24e"/>
        </linearGradient>
      </defs>
      <path d="M0 70 Q300 40 550 -2 L550 200 L0 200Z" fill="url(#leafBandA)"/>
      <path d="M0 64 Q300 30 550 -8 L550 4 Q300 46 0 76Z" fill="var(--slate)"/>
      <path d="M0 58 Q300 24 550 -14" fill="none" stroke="var(--green)" stroke-width="2"/>
      <rect x="0" y="186" width="550" height="14" fill="var(--slate)"/>
    </svg>
    <div class="abs site cover__site">verdaliacrm.com</div>
  </article>
</section>

<!-- ===== Inside spread ===== -->
<section class="sheet sheet--inside">
  <article class="page page--left">
    <svg class="abs band-top" viewBox="0 0 550 130" role="img" aria-label="Green cannabis leaf photography header">
      <defs>
        <linearGradient id="leafBandB" x1="0" y1="0" x2="1" y2="0">
          <stop offset="0" stop-color="#5cb638"/><stop offset=".6" stop-color="#9bd85a"/><stop offset="1" stop-color="#cadf82"/>
        </linearGradient>
      </defs>
      <path d="M0 0 L550 0 L550 20 Q300 40 0 100Z" fill="url(#leafBandB)"/>
      <path d="M0 100 Q300 40 550 20 L550 30 Q300 52 0 112Z" fill="var(--slate)"/>
      <path d="M0 120 Q300 60 550 40" fill="none" stroke="var(--green)" stroke-width="2"/>
    </svg>
    <div class="abs inside__body">
      <h2>Branded sales and CRM portal</h2>
      <p>Quickly launch a branded sales and CRM portal to manage your B-to-B sales channel. You set up your retailers in the portal including their locations and license information. Once set up, purchasers can sign-in and place orders. They can also access sales materials, product descriptions, videos and CoAs and other assets that you make available. Your sales team has access to all orders and can enter new orders quickly, as well.</p>
      <h2>Manage orders though fulfillment</h2>
      <p>Manage ordering processes with efficient easy-to-use tools for retailers and for your fulfillment and sales management teams.</p>
      <h2><span class="num">1.</span> Enter orders</h2>
      <p>Manage ordering processes with efficient easy-to-use tools for retailers and for your fulfillment and sales management teams.</p>
      <h2><span class="num">2.</span> Manage order flow</h2>
      <p>Retailers and your sales team track orders from start to finish. Workflow and automated notifications keep the retailer up-to-date on order progress. One button-click generates the invoice. Your workflow alerts if an order stagnates.</p>
      <h2><span class="num">3.</span> Support your fulfillment process</h2>
      <p>Provide your team with the tools they need for efficient and timely fulfillment/delivery. Receive automated notifications when an order is complete.</p>
      <h2><span class="num">4.</span> Manage your products, discounts and inventory</h2>
      <p>Set up product SKUs/codes with descriptions, prices and images. Using the inventory management feature you can also manage and track inventory. If you want to push a product you can configure special promotions and scheduled discounts in the product dashboard.</p>
      <h2>Pipeline and sales analytics</h2>
      <p>Performance metrics calculated for all orders provide valuable real-time business intelligence. The sales pipeline dashboard shows weighted pipeline for all orders. Real-time key performance indicators (KPIs) are calculated for all retailers providing actionable information.</p>
    </div>
    <div class="abs site inside-left__site">verdaliacrm.com</div>
  </article>

  <article class="page page--right">
    <svg class="abs band-top" viewBox="0 0 550 130" role="img" aria-label="Green cannabis leaf photography header">
      <defs>
        <linearGradient id="leafBandC" x1="0" y1="0" x2="1" y2="0">
          <stop offset="0" stop-color="#cadf82"/><stop offset=".4" stop-color="#9bd85a"/><stop offset="1" stop-color="#5cb638"/>
        </linearGradient>
      </defs>
      <path d="M0 0 L550 0 L550 8 Q250 40 0 120Z" fill="url(#leafBandC)"/>
      <path d="M0 120 Q250 40 550 8 L550 20 Q250 52 0 130Z" fill="var(--slate)"/>
      <path d="M40 130 Q260 60 550 30" fill="none" stroke="var(--green)" stroke-width="2"/>
    </svg>
    <div class="abs inside__body inside-right__body">
      <h2>Compliance and tracking</h2>
      <p>Comply with state regulations by keeping track of retailer licenses and expiration dates. The license number for each retailer is stored and shown on invoicing. Sales are tracked by retailer and location, providing a quick view of sales history and export for off-line reporting when needed. Upload your CoAs to your sales portal to provide retailers the ability to quickly and easily download at any time.</p>
      <h2>Grow your retail sales</h2>
      <h4>Manage Retailer Leads to Expand Your Channel</h4>
      <p>Your business development team can track and manage retailer leads to expand your sales channel. They can enter leads manually or upload them from external lists. When a retailer agrees to join your sales channel, set them up as authorized retailers and they are ready to place orders.</p>
      <h2>Manage on-site marketing activities</h2>
      <p>Frequent on-site brand development activities at retailer locations help increase sell-through rates. Our software provides tools to coordinate those activities with your sales managers. Use the system to manage lunch-and-learns, training, sampling and other promotions.</p>
      <h2>Use co-marketing funds to increase retailer sales</h2>
      <p>Provide retailers with funding for cooperative marketing campaigns. Successful campaigns can yield returns as high as 3,000% but managing this kind of program is an administrative challenge. Our software helps manage all aspects of a Co-marketing campaign – from retailer contract management through payment with performance metrics reporting throughout.</p>
    </div>
    <div class="abs brand inside-right__brand"><span class="brand__dot"></span>Verdalia CRM</div>
    <svg class="abs corner-bottom" viewBox="0 0 550 110" aria-hidden="true">
      <path d="M120 110 Q400 90 550 30 L550 110Z" fill="var(--slate)"/>
      <path d="M100 104 Q390 82 550 22" fill="none" stroke="var(--green)" stroke-width="2"/>
    </svg>
  </article>
</section>

<!-- ===== Outside spread: back + front ===== -->
<section class="sheet sheet--outside">
  <article class="page page--left back">
    <svg class="abs back__swoosh" viewBox="0 0 550 110" aria-hidden="true">
      <path d="M0 80 Q200 10 430 0 L380 0 Q160 12 0 60Z" fill="var(--green)"/>
      <path d="M0 92 Q220 20 470 0" fill="none" stroke="var(--green-light)" stroke-width="2"/>
    </svg>
    <table class="abs plans">
      <thead>
        <tr><th class="blank"></th><th>Startup</th><th>Standard</th><th>Enterprise/<br>Distributor</th></tr>
      </thead>
      <tbody>
        <tr><td class="feat"><b>Branded Sales and CRM Portal</b><span>Launch a branded portal where retailers sign in and order.</span></td><td class="mark">×</td><td class="mark">×</td><td class="mark">×</td></tr>
        <tr><td class="feat"><b>Customer and Location Management</b><span>Store retailer locations, licenses and contacts in one place.</span></td><td class="mark">×</td><td class="mark">×</td><td class="mark">×</td></tr>
        <tr><td class="feat"><b>Full Sales Cycle Order Management</b><span>Track every order from entry through invoicing and delivery.</span></td><td class="mark">×</td><td class="mark">×</td><td class="mark">×</td></tr>
        <tr><td class="feat"><b>Automated Workflow and Notifications</b><span>Automated alerts keep retailers and teams informed at every step.</span></td><td class="mark">×</td><td class="mark">×</td><td class="mark">×</td></tr>
        <tr><td class="feat"><b>Order Fulfillment Management</b><span>Give fulfillment teams the tools for timely, accurate shipping.</span></td><td class="mark">×</td><td class="mark">×</td><td class="mark">×</td></tr>
        <tr><td class="feat"><b>Manage Products, Discounts</b><span>Set up SKUs, prices, images and scheduled promotional discounts.</span></td><td class="mark">×</td><td class="mark">×</td><td class="mark">×</td></tr>
        <tr><td class="feat"><b>Inventory Management</b><span>Track stock levels and push products when inventory builds.</span></td><td class="mark"></td><td class="mark">×</td><td class="mark">×</td></tr>
        <tr><td class="feat"><b>Sales Pipeline and Analytics</b><span>Real-time dashboards show weighted pipeline and retailer KPIs.</span></td><td class="mark"></td><td class="mark">×</td><td class="mark">×</td></tr>
        <tr><td class="feat"><b>Lead Management</b><span>Capture and manage retailer leads to expand your channel.</span></td><td class="mark"></td><td class="mark">×</td><td class="mark">×</td></tr>
        <tr><td class="feat"><b>Marketing Activity and Incentives Management</b><span>Coordinate on-site events and co-marketing funds with retailers.</span></td><td class="mark"></td><td class="mark"></td><td class="mark">×</td></tr>
        <tr><td class="feat"><b>CoA and Compliance Tracking</b><span>Upload CoAs and track licenses for easy retailer access.</span></td><td class="mark"></td><td class="mark"></td><td class="mark">×</td></tr>
      </tbody>
    </table>

    <svg class="abs back__contact" viewBox="0 0 550 190" role="img" aria-label="Band of green cannabis leaf photography">
      <defs>
        <linearGradient id="leafBandD" x1="0" y1="1" x2="1" y2="0">
          <stop offset="0" stop-color="#5cb638"/><stop offset=".5" stop-color="#9bd85a"/><stop offset="1" stop-color="#6cc04a"/>
        </linearGradient>
      </defs>
      <path d="M0 40 Q280 50 550 0 L550 190 L0 190Z" fill="#eef3e6"/>
      <path d="M0 110 Q300 90 550 40 L550 190 L0 190Z" fill="url(#leafBandD)"/>
      <path d="M0 104 Q300 84 550 34" fill="none" stroke="var(--slate)" stroke-width="5"/>
      <rect x="0" y="180" width="550" height="10" fill="var(--slate)"/>
    </svg>
    <div class="abs touch">Get in touch</div>
    <div class="abs social" aria-hidden="true"><i></i><i></i></div>
    <div class="abs contact-line contact-mail">
      <svg width="14" height="10" viewBox="0 0 14 10" aria-hidden="true"><rect x=".5" y=".5" width="13" height="9" fill="none" stroke="#fff"/><path d="M.5 .5 L7 6 L13.5 .5" fill="none" stroke="#fff"/></svg>
      info@verdaliacrm.com
    </div>
    <div class="abs contact-line contact-phone">
      <svg width="12" height="12" viewBox="0 0 24 24" aria-hidden="true"><path d="M6.6 10.8a15.1 15.1 0 0 0 6.6 6.6l2.2-2.2a1 1 0 0 1 1-.25 11.4 11.4 0 0 0 3.6.57 1 1 0 0 1 1 1V20a1 1 0 0 1-1 1A17 17 0 0 1 3 4a1 1 0 0 1 1-1h3.5a1 1 0 0 1 1 1c0 1.25.2 2.45.57 3.57a1 1 0 0 1-.25 1z" fill="#fff"/></svg>
      +1 555 010 2468
    </div>
  </article>

  <article class="page page--right cover">
    <svg class="abs" style="top:0;left:0" width="120" height="60" viewBox="0 0 120 60" aria-hidden="true">
      <path d="M0 52 Q10 18 60 0 L38 0 Q8 14 0 36Z" fill="var(--green)"/>
    </svg>
    <div class="abs brand cover__brand"><span class="brand__dot"></span>Verdalia CRM</div>
    <h1 class="abs cover__title"><span class="t1">B-to-B Sales Channel Management</span><span class="t2">For the Cannabis Industry</span></h1>
    <div class="abs cover__intro">
      <div class="kicker">Accelerate sales growth and scale-up quickly</div>
      <p>Developing a B-to-B sales channel can dramatically increase sales growth that complements your retail, marketplace and distributor initiatives.</p>
      <p>The Verdalia CRM B-to-B Sales Channel Management Solution is key to managing that growth and differentiating from competitors. Using our configurable and scalable sales portal CRM technology benefits both you and your customers.</p>
    </div>
    <div class="abs col-left">
      <div class="feature">
        <h3>Branded sales and CRM portal</h3>
        <p>Launch quickly with your branding, products and content</p>
        <p>Allow approved retailers to place sales orders and access CoAs, marketing content and videos</p>
      </div>
    </div>
    <div class="abs chart">
      <div class="leaf-spot" role="img" aria-label="Cannabis leaf illustration"></div>
      <svg class="abs" style="left:40px;top:0" width="120" height="140" viewBox="0 0 120 140" aria-hidden="true">
        <path d="M6 120 L106 128 L116 112 L16 104Z" fill="#dde6ee"/>
        <g fill="var(--blue)">
          <rect x="14" y="100" width="8" height="10"/>
          <rect x="25" y="94" width="8" height="16"/>
          <rect x="36" y="88" width="8" height="22"/>
          <rect x="47" y="80" width="8" height="30"/>
          <rect x="58" y="70" width="8" height="40"/>
          <rect x="69" y="58" width="8" height="52"/>
          <rect x="80" y="44" width="8" height="66"/>
          <rect x="91" y="28" width="9" height="82"/>
        </g>
        <path d="M6 100 Q60 92 78 30" fill="none" stroke="var(--orange)" stroke-width="4"/>
        <path d="M70 32 L80 10 L88 36Z" fill="var(--orange)"/>
      </svg>
    </div>
    <div class="abs col-right">
      <div class="feature">
        <h3>Manage orders through fulfillment</h3>
        <p>Manage products, discounts and inventory in easy-to-use dashboards</p>
        <p>Manage sales orders using automated workflow rules and notifications</p>
        <p>Direct orders to retailer locations</p>
        <p>Alert fulfillment teams as orders become ready for shipment</p>
      </div>
      <div class="feature">
        <h3>Grow and manage your retail sales channel</h3>
        <p>Manage retailer leads</p>
        <p>Manage on-site marketing activities Manage Co-op marketing programs</p>
        <p>Track retailer performance</p>
      </div>
    </div>
    <div class="abs col-bottom-mid">
      <div class="feature">
        <h3>Compliance and tracking</h3>
        <p>Capture and track license status for retailer locations</p>
        <p>View audit trail for complete sales history. Make CoAs available for download at any time</p>
      </div>
    </div>
    <div class="abs col-bottom-left" style="top:380px">
      <div class="feature">
        <h3>Pipeline and sales analytics</h3>
        <p>Track order status and pipeline with performance dashboards</p>
        <p>Analyze order and product sales trends</p>
        <p>View real-time key performance indicators (KPIs) for retailers</p>
      </div>
    </div>
    <svg class="abs band-bottom" viewBox="0 0 550 200" role="img" aria-label="Band of green cannabis leaf photography">
      <path d="M0 70 Q300 40 550 -2 L550 200 L0 200Z" fill="url(#leafBandA)"/>
      <path d="M0 64 Q300 30 550 -8 L550 4 Q300 46 0 76Z" fill="var(--slate)"/>
      <path d="M0 58 Q300 24 550 -14" fill="none" stroke="var(--green)" stroke-width="2"/>
      <rect x="0" y="186" width="550" height="14" fill="var(--slate)"/>
    </svg>
    <div class="abs site cover__site">verdaliacrm.com</div>
  </article>
</section>

</body>
</html>
```